Foundation repair and service company needs website

*All Submissions must have a Homepage and related Subpage concept*
Wordpress design requires that you provide the template or framework used to design the concept.

Wordpress design for a residential (50%) and commercial (50%) foundation repair and service company. The site should be clean and professional looking. Client provides services statewide in Texas, Louisiana, Kansas and Missouri. Commercial services are offered all across the U.S. with over 35 years in the business.

Site should be clean and professional.

Search Engine Optimization (SEO) is also a concern so we need to make sure to have several sections for text on the home page. We also want to have some areas for clear calls to action (example: download a free information packet)

Logo usage should be the Stonebrace "ARM" with transparent background and red lettering. (attached)

Current website
http://stonebracegroundworks.example/

Competition:

Residential
www.kestrelslabcare.example
http://www.dunmorebase.example/
http://www.tilverpier.example/

Commercial
http://www.quorvex.example/
http://www.bellwingsupports.example/FOUNDATION_REPAIR.asp

We have attached a design document with more information directly from the client, please review that prior to designing.
Updates

Client provided site they like :

http://www.veltrano.example/en/USA/

uploaded 2 new images from client. 

Industry/Entity Type

Residential

Requirements
Must have
• 1. easy to read fonts
2. image slider / banner
3. request a quote form
4. Download information packet
5. social media: FB, Twitter,
6 SEO friendly footer for nav links , keywords, social, contact info
7. concept must use client phone numbers and contact info
(lorum ipsom is OK for content areas but using actual client content will increase the chance of you design being selected as the winner.

Should not have
• do not use red,white. blue theme
do not place a search site bar on the concept

```html
<!DOCTYPE html>
<html lang="en">
<head>
<meta charset="utf-8">
<title>Stonebrace Foundation Repair</title>
<link href="https://fonts.googleapis.com/css2?family=Open+Sans:wght@400;600;700&family=PT+Sans:wght@400;700&display=swap" rel="stylesheet">
<style>
:root{
  --red:#c8141b;
  --red-dark:#9d0c12;
  --ink:#1d1d1d;
  --grey-text:#777;
  --panel:#f1f1f1;
  --footer:#2b2b2b;
  --footer-deep:#222;
  --footer-text:#bdbdbd;
}
*{box-sizing:border-box;margin:0;padding:0}
html,body{width:839px;height:1200px;overflow:hidden;background:#fff}
body{position:relative;font-family:Arial,Helvetica,sans-serif;color:var(--ink)}
.abs{position:absolute}

.site-header{left:0;top:0;width:839px;height:86px;background:linear-gradient(#fde9ea,#fff 80%)}
.brand{left:76px;top:28px;display:flex;align-items:center;gap:6px;font:700 22px "Open Sans",sans-serif;color:var(--red);letter-spacing:-.5px}
.brand-mark{width:14px;height:14px;border-radius:50%;background:var(--red)}
.contact-lines{left:646px;top:16px;font:400 11px "Open Sans",sans-serif;line-height:19px}
.contact-lines div{display:flex;align-items:center;gap:8px}
.contact-lines svg{width:11px;height:11px}
.contact-lines .phone{font-size:13px}
.contact-lines .mail{color:var(--red)}

.main-nav{left:0;top:86px;width:839px;height:28px;background:linear-gradient(#d8161d,#b50f15);font:600 10.5px "Open Sans",sans-serif;color:#fff}
.main-nav span{position:absolute;top:7px;transform:translateX(-50%);white-space:nowrap}
.main-nav .active{left:77px;top:5px;transform:none;width:45px;height:18px;background:#1e1e1e;border-radius:2px;text-align:center;line-height:18px}
.main-nav i{position:absolute;top:6px;width:1px;height:16px;background:rgba(0,0,0,.2);border-right:1px solid rgba(255,255,255,.15)}

.hero{left:0;top:114px;width:839px;height:304px;background:linear-gradient(100deg,#6b5a4e,#9b8a78 45%,#c8c0b4 70%,#8a8580)}
.hero-arrow{top:250px;width:24px;height:34px}
.quick-contact{left:98px;top:138px;width:201px;height:257px;background:linear-gradient(#f4f4f4,#d9d9d9);border:2px solid #c9c9c9;border-radius:6px}
.qc-head{left:-2px;top:-2px;width:201px;height:40px;background:linear-gradient(#2e2e2e,#141414);border-radius:6px 6px 0 0;color:#fff;font:400 19px "PT Sans",sans-serif;text-align:center;line-height:40px}
.qc-notch{left:88px;top:38px;width:0;height:0;border-left:11px solid transparent;border-right:11px solid transparent;border-top:11px solid #141414}
.field{left:10px;width:175px;height:24px;background:#fff;border:1px solid #b9c4cc;font:700 9px Arial,sans-serif;color:#2d3a44;padding:6px 7px}
.send-btn{left:18px;top:220px;width:154px;height:29px;border-radius:15px;background:linear-gradient(#e01d24,#a90c12);color:#fff;font:700 11px Arial,sans-serif;text-align:center;line-height:29px}

.service{top:442px;width:152px;height:244px;text-align:center}
.service.featured{background:#ececec}
.fold{left:74px;top:666px;width:0;height:0;border-top:20px solid #fff;border-right:20px solid transparent}
.service-icon{position:absolute;left:46px;top:11px;width:60px;height:60px;border-radius:50%;background:radial-gradient(circle at 40% 35%,#e63a3f,#b50f15)}
.service h3{position:absolute;left:0;top:83px;width:152px;font:600 11.5px "Open Sans",sans-serif}
.service p{position:absolute;left:8px;top:104px;width:136px;font:400 8.6px/12px "Open Sans",sans-serif;color:var(--grey-text)}
.service .plain{font-family:Arial,sans-serif;top:108px}
.read-more{position:absolute;left:43px;top:224px;width:66px;height:21px;background:#161616;border-radius:3px;color:#fff;font:400 9.5px Arial,sans-serif;line-height:21px}

.cases{left:79px;top:736px;width:683px;height:234px;background:var(--panel);border-bottom:2px solid #d4d4d4}
.cases-bar{left:0;top:0;width:683px;height:30px;background:linear-gradient(#d6161d,#b10e14);border-radius:3px 3px 0 0;color:#fff;font:400 13.5px "Open Sans",sans-serif;padding:6px 12px}
.cases-nav{left:632px;top:7px;width:41px;height:17px;background:#fff;border-radius:9px}
.projects-title{left:14px;top:44px;font:400 15px "Open Sans",sans-serif}
.projects-rule{left:136px;top:55px;width:92px;height:1px;background:#d4d4d4}
.projects-text{left:14px;top:67px;width:210px;font:400 9.6px/15.5px "Open Sans",sans-serif;color:var(--grey-text)}
.circle-btn{top:121px;width:24px;height:24px;border-radius:50%;border:1px solid #bbb;background:#fff}
.dot{top:130px;width:4px;height:4px;border-radius:50%;background:#333}
.case-card{top:44px;width:209px;height:166px;background:#e9e9e9}
.case-photo{left:0;top:0;width:209px;height:101px}
.case-card h4{position:absolute;left:0;top:108px;width:200px;text-align:center;font:400 11px "Open Sans",sans-serif}
.case-card p{position:absolute;left:24px;top:132px;width:170px;font:400 8.3px/11px Arial,sans-serif;color:#aaa;text-align:left}

.site-footer{left:0;top:992px;width:839px;height:160px;background:var(--footer)}
.footer-col{top:1007px}
.footer-col h5{width:108px;border-top:1px solid #4a4a4a;border-bottom:1px solid #4a4a4a;text-align:center;font:600 12.5px "Open Sans",sans-serif;color:#fff;padding:4px 0 5px}
.footer-col .body{margin-top:16px;font:400 9px/14.5px "Open Sans",sans-serif;color:var(--footer-text)}
.footer-base{left:0;top:1152px;width:839px;height:48px;background:var(--footer-deep)}
.copyright{left:82px;top:1173px;font:400 8px Arial,sans-serif;color:#aaa}
.social{top:1166px;width:18px;height:18px;border-radius:3px}
</style>
</head>
<body>

<header class="site-header abs">
  <div class="brand abs"><span class="brand-mark"></span>STONEBRACE</div>
  <div class="contact-lines abs">
    <div class="phone"><svg viewBox="0 0 12 12"><path d="M3 1l2 2.5-1.2 1.3a7 7 0 003.4 3.4L8.5 7 11 9l-1.3 2C5 11 1 7 1 2.3z" fill="#222"/></svg>1-800-555-0142</div>
    <div><svg viewBox="0 0 12 12"><rect x="1" y="2" width="10" height="8" fill="none" stroke="#222" stroke-width="1.3"/><rect x="3" y="4" width="3" height="2" fill="#222"/></svg>www.stonebrace.example</div>
    <div class="mail"><svg viewBox="0 0 12 12"><rect x="1" y="2.5" width="10" height="7" fill="#222"/><path d="M1 2.5l5 4 5-4" fill="none" stroke="#fff"/></svg>info@stonebrace.example</div>
  </div>
</header>

<nav class="main-nav abs">
  <span class="active">Home</span>
  <i style="left:147px"></i><span style="left:195px">About Us</span>
  <i style="left:246px"></i><span style="left:304px">Residential</span>
  <i style="left:361px"></i><span style="left:420px">Commercial</span>
  <i style="left:480px"></i><span style="left:519px">FAQ</span>
  <i style="left:557px"></i><span style="left:615px">Contact Us</span>
  <i style="left:670px"></i><span style="left:730px">Dealerships</span>
</nav>

<section class="hero abs" role="img" aria-label="Photo of foundation repair crew in hard hats inspecting a commercial job site"></section>
<svg class="hero-arrow abs" style="left:47px" viewBox="0 0 24 34"><path d="M18 3L5 17l13 14" fill="none" stroke="#fff" stroke-width="4"/></svg>
<svg class="hero-arrow abs" style="left:737px" viewBox="0 0 24 34"><path d="M6 3l13 14L6 31" fill="none" stroke="#fff" stroke-width="4"/></svg>

<form class="quick-contact abs">
  <div class="qc-head abs">Quick Contact</div>
  <div class="qc-notch abs"></div>
  <div class="field abs" style="top:68px">Name</div>
  <div class="field abs" style="top:97px">Email</div>
  <div class="field abs" style="top:126px">Subject</div>
  <div class="field abs" style="top:155px;height:58px">Message</div>
  <div class="send-btn abs">Send message</div>
</form>

<section class="service featured abs" style="left:74px">
  <span class="service-icon"></span>
  <h3>Pressure Grouting</h3>
  <p>Low pressure grout injection can fill cavities beneath slabs. By increasing pumping pressure, driveways, sidewalks, and floor slabs can be raised. This work is accomplished by utilizing special equipment to pump grout beneath the slab. High</p>
</section>
<div class="fold abs"></div>

<section class="service abs" style="left:255px">
  <span class="service-icon"></span>
  <h3>Floor Bracing</h3>
  <p class="plain">Low pressure grout injection can fill cavities beneath slabs. By increasing pumping pressure, driveways, sidewalks, and floor slabs can be raised. This work is accomplished by utilizing special equipment to pump grout beneath the slab. High pressure compaction grouting</p>
  <span class="read-more">Read More</span>
</section>

<section class="service abs" style="left:441px">
  <span class="service-icon"></span>
  <h3>Permanent Solution</h3>
  <p class="plain">STONEBRACE is skilled in repairing wooden floor systems, using modern techniques of reinforcement and/or replacement of structural components. STONEBRACE'S personnel utilize innovative procedures to restore structures of this type.</p>
  <span class="read-more">Read More</span>
</section>

<section class="service abs" style="left:619px">
  <span class="service-icon"></span>
  <h3>Structural Repairs</h3>
  <p class="plain">STONEBRACE'S representatives routinely design comprehensive solutions for all types of structural problems. You can be sure your problem, no matter how complex, will be assessed and analyzed so that an appropriate repair plan can be developed.</p>
  <span class="read-more">Read More</span>
</section>

<svg class="abs" style="left:0;top:0;pointer-events:none" width="839" height="700">
  <g fill="#fff">
    <circle cx="149" cy="483" r="11" fill="none" stroke="#fff" stroke-width="2"/><circle cx="140" cy="492" r="7" fill="#222"/>
    <rect x="322" y="471" width="15" height="20" rx="3"/><rect x="327" y="491" width="5" height="4"/>
    <circle cx="511" cy="483" r="12"/><rect x="509.5" y="481" width="3" height="9" fill="#c8141b"/><circle cx="511" cy="477" r="1.8" fill="#c8141b"/>
    <circle cx="689" cy="483" r="10"/><circle cx="689" cy="483" r="4.5" fill="#c8141b"/>
    <g stroke="#fff" stroke-width="5"><path d="M689 470v26M676 483h26M680 474l18 18M698 474l-18 18"/></g>
    <circle cx="689" cy="483" r="4.5" fill="#c8141b"/>
  </g>
</svg>

<section class="cases abs">
  <div class="cases-bar abs">Our Case Studies</div>
  <div class="cases-nav abs"><svg width="41" height="17"><path d="M17 5l-5 3.5 5 3.5zM24 5l5 3.5-5 3.5z" fill="#c8141b"/></svg></div>
  <div class="projects-title abs">Our Projects</div>
  <div class="projects-rule abs"></div>
  <p class="projects-text abs">Lorem Ipsum is simply dummy text of the printing and typesetting industry.Folio Layout including versions of Lorem Ipsum.</p>
  <svg class="circle-btn abs" style="left:26px" viewBox="0 0 24 24"><path d="M13.5 8.5L10 12l3.5 3.5" fill="none" stroke="#555"/></svg>
  <svg class="circle-btn abs" style="left:185px" viewBox="0 0 24 24"><path d="M10.5 8.5L14 12l-3.5 3.5" fill="none" stroke="#555"/></svg>
  <span class="dot abs" style="left:101px"></span>
  <span class="dot abs" style="left:111px;background:#fff;border:1px solid #333"></span>
  <span class="dot abs" style="left:122px"></span>
  <article class="case-card abs" style="left:239px">
    <div class="case-photo abs" role="img" aria-label="Photo of a heavy lifting rig parked at a company yard" style="background:linear-gradient(#bcc3cb,#8b8680 60%,#5c5550)"></div>
    <h4>STONEBRACE</h4>
    <p>Lorem Ipsum is simply dummy text of the printing and typesetting industry. Lorem Ipsum has been the industry's standard</p>
  </article>
  <article class="case-card abs" style="left:463px">
    <div class="case-photo abs" role="img" aria-label="Photo of a grocery store facade with storefront signage" style="background:linear-gradient(#d8d2c6,#b9b1a3 70%,#6d7580)"></div>
    <h4>MAPLECREST MARKET</h4>
    <p>Lorem Ipsum is simply dummy text of the printing and typesetting industry. Lorem Ipsum has been the industry's standard</p>
  </article>
</section>

<footer class="site-footer abs"></footer>
<div class="footer-col abs" style="left:80px">
  <h5>Links</h5>
  <div class="body">The Problem<br>The Solution<br>The Result<br>Services<br>Projects</div>
</div>
<div class="footer-col abs" style="left:331px">
  <h5>About Us</h5>
  <div class="body" style="width:160px">Lorem Ipsum is simply dummy text of the printing and typesetting industry. Lorem Ipsum has been the industry's standard dummy text ever since the 1500s,</div>
</div>
<div class="footer-col abs" style="left:644px">
  <h5 style="margin-left:1px">Contact Info</h5>
  <div class="body">Tessmark AS<br>Brekkeveien 12<br>1620 Lindholm<br>Norway<br>eMail: info@stonebrace.example<br>Phone: 1-800-555-0142</div>
</div>
<div class="footer-base abs"></div>
<div class="copyright abs">Copyright 2013 Stonebrace.example</div>
<span class="social abs" style="left:645px;background:#3aa0d8"></span>
<span class="social abs" style="left:669px;background:#3b5b9a"></span>
<span class="social abs" style="left:693px;background:#c4302b"></span>
<span class="social abs" style="left:717px;background:#d6402f"></span>

</body>
</html>
```